CalmPath Nurses' Manifesto

Design a manifesto to inspire and motivate nurses to work at minimum standards of excellence in their nursing practice.

The manifesto will become a feature of our website, at conferences, workshops and retreats. It will also be featured on other marketing tools.

Primary Market:
Nurses and/or other healthcare professionals (specifically Doctors, Occupational Therapists, Psychologists and Social Workers).

However the manifesto is equally applicable to all nurses and healthcare professionals from new graduates to very experienced senior clinicians, administration officers,managers and healthcare executive personnel.

Mainly females and primarily 35 to 65 years old, which suggests people in this target age group have extensive experience, but have become jaded'.

The purpose of our business is to assist healthcare professionals, primarily nurses, to maintain their enthusiasm and excellence in service provision, for their benefit as well as the benefit of the clients.

I have attached:
File 1: Copy Samples and examples: which has the copy for the manifesto, examples that appeal to us and our 3 attempts.
File 2: Our colour Spec Sheet, HOWEVER the colours are not necessary limited to these colours. These colours are not in the logo that will be on the manifesto. The colours on the logo attached can/or also be used.
File 3: Prototype logo. The final logo will be available within 3 to 4 days.

Requirements
Must have
• Must use the copy as per the attached file.

It should be contemporary, eye catching and motivational.

Sample 1 on the attached file (File 3: copy, samples and examples_554207 saturday, 29 june 2013 06:24:3030) Is close to what we are looking for.
Should not have
• MUST BE EASY TO READ. Each line MUST be clearly defined from each other.

```html
<!DOCTYPE html>
<html lang="en">
<head>
<meta charset="utf-8">
<title>CalmPath Nurses' Manifesto</title>
<link href="https://fonts.googleapis.com/css2?family=Alfa+Slab+One&family=Mukta:wght@500&family=Nunito:wght@800&family=Roboto+Slab:wght@700&family=Archivo+Black&family=Courgette&family=Black+Ops+One&family=Russo+One&family=Open+Sans:wght@400;700&family=Comfortaa:wght@500&family=Share+Tech+Mono&family=Inconsolata:wght@600&family=Michroma&family=Orbitron:wght@500&family=Tinos&display=swap" rel="stylesheet">
<style>
  :root {
    --board: #3c5557;
    --white: #ffffff;
    --orange: #f2954b;
    --lime: #a4c93f;
    --grey: #a9abab;
    --green: #45b26b;
    --teal: #4cb1aa;
    --teal-soft: #62b9ae;
  }
  html, body { margin: 0; padding: 0; overflow: hidden; }
  body { width: 900px; height: 1200px; background: var(--board); }
  .manifesto { position: relative; width: 900px; height: 1200px; background: var(--board); overflow: hidden; }
  .line { position: absolute; margin: 0; white-space: nowrap; line-height: 1; }

  .title { left: 62px; top: 28px; width: 776px; display: flex; align-items: center; justify-content: center; gap: 18px; }
  .title-text { font-family: "Alfa Slab One", serif; font-size: 38px; color: var(--white); letter-spacing: 1.5px; font-weight: 400; margin: 0; }
  .rule { width: 60px; height: 14px; }

  .open-hands { left: 68px; top: 80px; font-family: "Mukta", sans-serif; font-weight: 500; font-size: 42px; color: var(--orange); }
  .delight { left: 68px; top: 134px; font-family: "Nunito", sans-serif; font-weight: 800; font-size: 35px; color: var(--lime); }
  .learn { left: 68px; top: 172px; font-family: "Roboto Slab", serif; font-weight: 700; font-size: 50px; color: var(--grey); }
  .exceeding { left: 232px; top: 178px; font-family: "Nunito", sans-serif; font-weight: 800; font-size: 35px; color: var(--lime); }
  .something { left: 68px; top: 210px; font-family: "Roboto Slab", serif; font-weight: 700; font-size: 54px; letter-spacing: 1px; color: var(--grey); }
  .support { left: 68px; top: 274px; font-family: "Archivo Black", sans-serif; font-size: 43px; color: var(--white); line-height: 1.1; }
  .trust { left: 68px; top: 384px; font-family: "Courgette", cursive; font-size: 39px; color: var(--lime); line-height: 1.15; }
  .trust .big { font-size: 50px; }
  .lifelong { left: 68px; top: 478px; font-family: "Archivo Black", sans-serif; font-size: 56px; color: var(--orange); }
  .celebrate { left: 68px; top: 544px; font-family: "Black Ops One", sans-serif; font-size: 28px; color: var(--green); line-height: 1.05; letter-spacing: 4.4px; }
  .unique { left: 68px; top: 608px; font-family: "Russo One", sans-serif; font-size: 21px; color: var(--teal); }
  .unique .big { font-size: 38px; }
  .revel { left: 68px; top: 670px; font-family: "Russo One", sans-serif; font-size: 22px; color: var(--teal); }
  .right-thing { left: 332px; top: 610px; font-family: "Open Sans", sans-serif; font-size: 27px; color: var(--white); }
  .exception { left: 466px; top: 624px; font-family: "Open Sans", sans-serif; font-size: 68px; color: var(--white); }
  .within { left: 68px; top: 700px; font-family: "Comfortaa", sans-serif; font-weight: 500; font-size: 41px; color: var(--lime); }
  .follow { left: 70px; top: 756px; font-family: "Share Tech Mono", monospace; font-size: 22px; color: var(--teal-soft); letter-spacing: 10.5px; }
  .no-one { left: 70px; top: 790px; font-family: "Inconsolata", monospace; font-weight: 600; font-size: 22px; color: var(--lime); letter-spacing: 2.8px; }
  .no-one .big { font-size: 44px; font-family: "Comfortaa", sans-serif; letter-spacing: 1px; vertical-align: -6px; }
  .purpose { left: 70px; top: 830px; font-family: "Mukta", sans-serif; font-weight: 500; font-size: 30px; letter-spacing: 0.5px; color: var(--orange); }
  .respond { left: 70px; top: 862px; font-family: "Michroma", sans-serif; font-size: 30px; color: var(--white); line-height: 1.33; letter-spacing: 1.2px; }
  .respond .c-orange { color: var(--orange); }
  .respond .c-teal { color: var(--teal); }
  .respond .c-lime { color: var(--lime); }
  .can-do { left: 72px; top: 984px; font-family: "Open Sans", sans-serif; font-weight: 700; font-size: 21px; color: var(--lime); letter-spacing: 0.3px; }
  .choose { left: 72px; top: 1030px; font-family: "Orbitron", sans-serif; font-weight: 500; font-size: 29px; color: var(--green); line-height: 1.95; letter-spacing: 1px; }
  .reality { left: 560px; top: 1070px; font-family: "Michroma", sans-serif; font-size: 35px; color: var(--orange); }
  .deliver { left: 66px; top: 1136px; font-family: "Open Sans", sans-serif; font-weight: 700; font-size: 28px; color: var(--white); }
  .live { left: 562px; top: 1136px; font-family: "Open Sans", sans-serif; font-weight: 700; font-size: 28px; color: var(--white); }

  .brand { position: absolute; left: 388px; top: 1104px; display: flex; align-items: center; gap: 8px; }
  .brand-dot { width: 22px; height: 22px; border-radius: 50%; background: var(--teal); }
  .brand-name { font-family: "Open Sans", sans-serif; font-weight: 700; font-size: 20px; color: var(--white); line-height: 1; margin: 0; }

  .vertical { position: absolute; margin: 0; white-space: nowrap; writing-mode: vertical-rl; line-height: 1; }
  .up { transform: rotate(180deg); }
  .side-smile { left: 28px; top: 28px; height: 1142px; font-family: "Tinos", serif; font-size: 25px; letter-spacing: 3px; color: var(--white); text-align: right; }
  .side-smile .small { font-family: "Open Sans", sans-serif; font-size: 22px; letter-spacing: 3.3px; }
  .side-health { left: 848px; top: 28px; height: 1142px; font-family: "Tinos", serif; font-size: 25px; letter-spacing: 3.3px; color: var(--white); text-align: right; }
  .side-respect { left: 786px; top: 130px; font-family: "Courgette", cursive; font-size: 36px; letter-spacing: 1.4px; color: var(--teal-soft); }
  .side-generous { left: 732px; top: 130px; font-family: "Courgette", cursive; font-size: 30px; color: var(--teal-soft); }
</style>
</head>
<body>
<main class="manifesto">
  <header class="line title">
    <svg class="rule" viewBox="0 0 60 14" aria-hidden="true"><line x1="2" y1="7" x2="58" y2="7" stroke="#fff" stroke-width="2"/><circle cx="8" cy="7" r="3" fill="#fff"/><circle cx="52" cy="7" r="3" fill="#fff"/></svg>
    <h1 class="title-text">NURSES' MANIFESTO</h1>
    <svg class="rule" viewBox="0 0 60 14" aria-hidden="true"><line x1="2" y1="7" x2="58" y2="7" stroke="#fff" stroke-width="2"/><circle cx="8" cy="7" r="3" fill="#fff"/><circle cx="52" cy="7" r="3" fill="#fff"/></svg>
  </header>

  <p class="line open-hands">Nurse with open hands, hearts and minds.</p>
  <p class="line delight">Delight your clients and colleagues by</p>
  <p class="line learn">Learn</p>
  <p class="line exceeding">exceeding their expectations.</p>
  <p class="line something">something new each day.</p>
  <p class="line support">Support your colleagues &amp;<br>champion their purpose.</p>
  <p class="line trust">Trust your <span class="big">knowledge</span> and seek<br>advice only from respected sources.</p>
  <p class="line lifelong">Be a life long learner.</p>
  <p class="line celebrate">CELEBRATE,RESPECT AND VALUE THE<br>DIVERSITY OF AUSTRALIAN CULTURE.</p>
  <p class="line unique">YOU ARE <span class="big">UNIQUE</span>,</p>
  <p class="line revel">REVEL IN YOUR INDIVIDUALITY.</p>
  <p class="line right-thing">Always do the right thing without</p>
  <p class="line exception">exception</p>
  <p class="line within">Seek success firstly from within.</p>
  <p class="line follow">ONLY FOLLOW EXCEPTIONAL LEADERS.</p>
  <p class="line no-one">If there is no one left to follow, then <span class="big">lead!</span></p>
  <p class="line purpose">Always lead with purpose,passion and commitment.</p>
  <p class="line respond">Respond to complex situations<br><span class="c-orange">innovatively</span>, <span class="c-teal">creatively</span> and <span class="c-lime">safely</span><br>within the scope of your practice.</p>
  <p class="line can-do">Adopt a‘can do’ attitude to everything that comes your way.</p>
  <p class="line choose">CHOOSE YOUR THOUGHTS WISELY, THEY<br>CREATE YOUR</p>
  <p class="line reality">REALITY.</p>
  <p class="line deliver">Delivercare skillfully.</p>
  <div class="brand">
    <span class="brand-dot" aria-hidden="true"></span>
    <p class="brand-name">CalmPath</p>
  </div>
  <p class="line live">Live your dream.</p>

  <p class="vertical up side-smile"><span class="small">Always be solution focused!</span> Smile and infect others with your happiness and have fun!</p>
  <p class="vertical up side-health">Look after yourself and value your health as much as you value the health of others.</p>
  <p class="vertical side-respect">Respect the limits of people's knowledge and share your</p>
  <p class="vertical side-generous">knowledge generously.</p>
</main>
</body>
</html>
```